Tr construction holdings pty ltd

2 sided card black and red with white
Very professional and elegant

Target Market(s)

Construction and Development

Industry/Entity Type

Construction and development

Contact Information for Business Card

One side black, one side red/or white business logo in top corner, email: morgan@trbuildworks.example

Requirements
Should not have
• Blue

```html
<!DOCTYPE html>
<html lang="en">
<head>
<meta charset="utf-8">
<title>TR Construction – Business Card</title>
<link rel="stylesheet" href="https://fonts.googleapis.com/css2?family=Open+Sans:ital,wght@0,400;0,700;1,400&display=swap">
<style>
  :root {
    --stage: #3b3b3b;
    --card: #262626;
    --card-edge: #2e2e2e;
    --red: #e8402a;
    --white: #ffffff;
    --muted: #d9d9d9;
    --pattern-dark: #1c1c1c;
    --pattern-light: #4a4a4a;
  }
  * { box-sizing: border-box; margin: 0; padding: 0; }
  html, body {
    width: 1200px; height: 900px; overflow: hidden;
    background: var(--stage);
    font-family: "Open Sans", Arial, sans-serif;
  }
  .sheet {
    width: 1200px; height: 900px;
    display: flex; flex-direction: column;
    align-items: center; justify-content: center; gap: 48px;
  }
  .card {
    width: 600px; height: 343px;
    border-radius: 18px;
    background: var(--card);
    position: relative; overflow: hidden;
    box-shadow: 0 14px 30px rgba(0,0,0,.35);
  }
  /* Front */
  .brand {
    position: absolute; left: 150px; top: 70px; width: 380px;
    text-align: center;
    font-weight: 700; font-size: 40px; letter-spacing: 1px;
    text-transform: uppercase; color: var(--white); line-height: 1.05;
  }
  .brand small { display: block; font-size: 24px; letter-spacing: 6px; margin-top: 6px; }
  .person {
    position: absolute; left: 44px; top: 218px; width: 210px; text-align: right;
  }
  .person-name {
    color: var(--red); font-weight: 700; font-size: 21px;
    text-transform: uppercase; letter-spacing: .5px;
  }
  .person-role { color: var(--white); font-style: italic; font-size: 14px; margin-top: 2px; }
  .divider {
    position: absolute; left: 272px; top: 210px;
    width: 1px; height: 78px; background: var(--muted);
  }
  .contact { position: absolute; left: 292px; top: 212px; list-style: none; }
  .contact li {
    display: flex; align-items: center; gap: 9px;
    color: var(--white); font-size: 14.5px; line-height: 25px;
  }
  .contact svg { width: 13px; height: 13px; fill: var(--red); flex: none; }
  /* Back */
  .pattern-field {
    position: absolute; inset: 0;
    background: linear-gradient(120deg, var(--pattern-dark) 0%, var(--card) 45%, var(--pattern-light) 100%);
  }
  .back-mark {
    position: absolute; right: 28px; bottom: 22px;
    color: var(--red); font-weight: 700; font-size: 16px;
    text-transform: uppercase; letter-spacing: 1px;
  }
</style>
</head>
<body>
<main class="sheet">
  <section class="card card-front" aria-label="Card front">
    <div class="brand">TR Construction<small>Holdings</small></div>
    <div class="person">
      <p class="person-name">Dana Whitfield</p>
      <p class="person-role">Managing Director</p>
    </div>
    <div class="divider"></div>
    <ul class="contact">
      <li><svg viewBox="0 0 24 24" aria-hidden="true"><path d="M6.6 10.8a15.1 15.1 0 0 0 6.6 6.6l2.2-2.2a1 1 0 0 1 1-.25 11.4 11.4 0 0 0 3.6.57 1 1 0 0 1 1 1V20a1 1 0 0 1-1 1A17 17 0 0 1 3 4a1 1 0 0 1 1-1h3.5a1 1 0 0 1 1 1c0 1.25.2 2.45.57 3.57a1 1 0 0 1-.25 1z"/></svg>+123 555 0148</li>
      <li><svg viewBox="0 0 24 24" aria-hidden="true"><path d="M2 5h20v14H2z M2 5l10 8 10-8" /></svg>morgan@trbuildworks.example</li>
      <li><svg viewBox="0 0 24 24" aria-hidden="true"><circle cx="12" cy="12" r="10"/></svg>www.trbuildworks.example</li>
    </ul>
  </section>

  <section class="card card-back" aria-label="Card back">
    <div class="pattern-field" role="img" aria-label="Repeating tone-on-tone monogram pattern across the card"></div>
    <p class="back-mark">TR Construction</p>
  </section>
</main>
</body>
</html>
```